Business Card Design Project

Looking for a cool, trendy design for new business cards for our Mobile Application business.

QuillNest Apps

www.quillnestapps.example

Target Market(s)

Looking for a bold modern design that attracts a younger demographic in the mobile space.

Industry/Entity Type

Business

Requirements
Must have
• Trendy, Easily adapted for other staff cards, works with large clients but showcases and innovative company

```html
<!DOCTYPE html>
<html lang="en">
<head>
<meta charset="utf-8">
<title>QuillNest Apps — Business Card</title>
<link rel="stylesheet" href="https://fonts.googleapis.com/css2?family=Marcellus&family=Fira+Sans+Condensed:ital,wght@1,100&family=Handlee&display=swap">
<style>
  :root {
    --stage-dark: #000000;
    --stage-grey: #808080;
    --card: #ffffff;
    --gold: #b89650;
    --ink: #333333;
    --label: #ffffff;
  }
  * { margin: 0; padding: 0; box-sizing: border-box; }
  html, body { width: 1200px; height: 1000px; overflow: hidden; }
  body { position: relative; font-family: "Marcellus", serif; }

  .stage { position: absolute; left: 0; width: 1200px; }
  .stage--dark { top: 0; height: 515px; background: var(--stage-dark); }
  .stage--grey { top: 515px; height: 485px; background: var(--stage-grey); }

  .card {
    position: absolute;
    width: 513px;
    height: 308px;
    background: var(--card);
    overflow: hidden;
  }
  .stage--dark .card { top: 72px; }
  .stage--grey .card { top: 48px; }
  .card--front { left: 52px; }
  .card--back { left: 631px; }

  .band {
    position: absolute;
    left: 0;
    top: 124px;
    width: 513px;
    height: 58px;
    background: var(--gold);
  }
  .band-text {
    position: absolute;
    left: 0;
    width: 513px;
    text-align: center;
    color: var(--card);
    white-space: nowrap;
  }
  .brand-name {
    top: 118px;
    font-size: 66px;
    line-height: 64px;
    letter-spacing: 3px;
  }
  .web-address {
    top: 121px;
    font-size: 33px;
    line-height: 64px;
  }
  .tagline {
    position: absolute;
    left: 0;
    top: 187px;
    width: 513px;
    text-align: center;
    font-family: "Handlee", cursive;
    font-size: 23px;
    color: var(--ink);
    white-space: nowrap;
  }

  .side-label {
    position: absolute;
    width: 513px;
    text-align: center;
    font-family: "Fira Sans Condensed", sans-serif;
    font-weight: 100;
    font-style: italic;
    font-size: 82px;
    line-height: 1;
    color: var(--label);
  }
  .stage--dark .side-label { top: 390px; }
  .stage--grey .side-label { top: 366px; }
  .side-label--front { left: 30px; }
  .side-label--back { left: 636px; }
</style>
</head>
<body>
  <section class="stage stage--dark">
    <article class="card card--front">
      <div class="band"></div>
      <p class="band-text brand-name">quillnest apps</p>
      <p class="tagline">mobile software for professional development</p>
    </article>
    <article class="card card--back">
      <div class="band"></div>
      <p class="band-text web-address">www.quillnestapps.example</p>
    </article>
    <p class="side-label side-label--front">Front</p>
    <p class="side-label side-label--back">Back</p>
  </section>

  <section class="stage stage--grey">
    <article class="card card--front">
      <div class="band"></div>
      <p class="band-text brand-name">quillnest apps</p>
      <p class="tagline">mobile software for professional development</p>
    </article>
    <article class="card card--back">
      <div class="band"></div>
      <p class="band-text web-address">www.quillnestapps.example</p>
    </article>
    <p class="side-label side-label--front">Front</p>
    <p class="side-label side-label--back">Back</p>
  </section>
</body>
</html>
```